We are a printed circuit board manufacturer. Need a company professional web site to allow our potential customers to know more about our background, capability and our products. The web site will contain three languages, which are Chinese, English and Japanese. Our audience are mainly electronic companies that procure printed circuit boards. I have a word document that have all the required text in all three languages. The final design should communicate the impression that we embrace quality, trustworthiness and long term partnership business principles.
We should have sections that allow us to post pictures of our facilities.
I have added the three files in three different languages.
Some of the information is below:
Background
RVD Worldwide Limited (RVD) was set up in Hong Kong in 2007 by two Hong Kong entrepreneurs, Mr. Lok Fai Tam and Mr. Wai Ho. We acquired the single sided printed circuit board factory located in Dongguan City, Guangdong Province, China, from Valtor Corporation of the U.S. in 2007. In addition to RVD, Mr. Tam and Mr. Ho also own Brightrail Systems Company Limited, a semiconductor company based in Hong Kong since 1997 with a total investment of over US$100 million. Brightrail is engaged in the manufacturing of flexible substrates and MEMS assembly business.
RVD has been awarded TS 16949 and ISO14000 certificates since 2009 and 2004 respectively.
Business Principles
RVD Worldwide Limited strives to be a professional top notched printed circuit board supplier. We embrace four “EXCELLENCE” principles, namely, excellence in quality, excellence in prices, excellence in services and excellence in on time delivery.
We approach each customer with a long-term partnership view that delivers the lowest ownership costs and highest total values to our customers. We customize quotations and solutions in order to allow our customers to win more businesses. We believe by thinking from our customers’ points of view we will be able to create a WIN-WIN relationship.
Customers
Due to our excellent quality, services and production systems, RVD Worldwide Limited manage to service a number of large Japanese and US customers, which include:
Technical capability overview
Below is an overview of our current capability:
Target Market(s)
Electronic companies buyers
Industry/Entity Type
Business
Requirements
Must have
- Capability description
Should not have
- no cartoon

```html
<!DOCTYPE html>
<html lang="en">
<head>
<meta charset="utf-8">
<title>RVD Worldwide Limited</title>
<link href="https://fonts.googleapis.com/css2?family=Cabin:wght@400;500;700&family=Lato:wght@300;400&family=Lora&family=Arimo&display=swap" rel="stylesheet">
<style>
:root{
  --green:#0f8a55;
  --green-dark:#086a40;
  --green-text:#0d7a4a;
  --ink:#222;
  --body:#555;
  --muted:#9a9a9a;
  --line:#cfcfcf;
  --footer-top:#4a4d51;
  --footer-bottom:#050505;
  --panel:#efefef;
}
*{box-sizing:border-box;margin:0;padding:0}
html,body{width:1050px;height:1200px;overflow:hidden}
body{position:relative;background:linear-gradient(#eaf3ef 0,#fff 160px,#fff);font-family:"Cabin",sans-serif;color:var(--ink)}
.abs{position:absolute}

.brand{left:106px;top:38px;width:200px;font-family:"Cabin",sans-serif;font-weight:700;font-size:24px;line-height:27px;color:var(--green-dark);display:flex;align-items:center;gap:8px;white-space:nowrap}
.brand-mark{width:14px;height:14px;background:var(--green-dark);flex:none}

.lang{left:669px;top:0;width:281px;height:29px;background:#fff;box-shadow:0 1px 3px rgba(0,0,0,.15);font-size:11px;display:flex;align-items:center;justify-content:flex-end;padding-right:20px;gap:12px}
.lang-select{border:1px solid #bbb;padding:1px 4px;color:var(--green-text);display:flex;gap:8px;align-items:center}
.lang-select span{display:inline-block;width:12px;height:12px;border:1px solid #777;position:relative}
.lang-select span:after{content:"";position:absolute;left:2px;top:4px;border:3px solid transparent;border-top-color:#222}

.contact-top{left:767px;top:48px;font-size:14px;line-height:22px;color:#222}
.contact-top div{display:flex;align-items:center;gap:8px}

.nav{left:96px;top:112px;width:858px;height:41px;background:linear-gradient(#149a60,#0a7446);border:1px solid #06552f;border-radius:3px;display:flex;align-items:center}
.nav-home{width:40px;height:41px;background:#1d1d1d;display:flex;align-items:center;justify-content:center;border-radius:3px 0 0 3px;margin-top:-1px}
.nav ul{list-style:none;display:flex;margin-left:6px}
.nav li{color:#fff;font-size:12px;padding:0 14.2px}

.hero{left:96px;top:165px;width:858px;height:310px;border-radius:6px;overflow:hidden;background:radial-gradient(circle at 60% 55%,#2b6f8c,#124a66 45%,#0b2d42);box-shadow:0 4px 8px rgba(0,0,0,.15)}
.hero-caption{position:absolute;left:0;bottom:0;width:100%;height:67px;background:rgba(20,20,20,.72);color:#fff;font-size:19px;line-height:19px;padding:13px 16px;letter-spacing:-.3px}

.welcome{left:96px;top:505px;font-family:"Lato",sans-serif;font-weight:300;font-size:31px;color:#222}
.welcome b{font-weight:400}
.about{left:100px;top:549px;width:552px;font-size:10.5px;line-height:15.75px;color:var(--body)}
.about p+p{margin-top:9px}
.btn{left:100px;top:681px;width:84px;height:31px;background:#1d1d1d;color:#fff;font-size:12.5px;display:flex;align-items:center;justify-content:center;border-radius:2px}

.clients{left:98px;top:738px;width:560px;height:161px;background:var(--panel);border:1px solid #cfcfcf;border-radius:4px}
.clients-tab{left:89px;top:738px;width:195px;height:30px;background:var(--green);color:#fff;font-size:13.5px;display:flex;align-items:center;padding-left:13px;z-index:2}
.clients-tab:after{content:"";position:absolute;left:0;bottom:-7px;border-left:8px solid transparent;border-top:7px solid #053a22}
.client{position:absolute;background:#fff;height:30px;display:flex;align-items:center;justify-content:center;font-family:"Cabin",sans-serif;font-weight:700;font-size:17px;color:#1d3f8a;white-space:nowrap}

.side-title{left:691px;top:508px;width:263px;font-family:"Lora",serif;font-size:20px;color:#444;border-bottom:1px dotted #bbb;padding-bottom:5px}
.item{position:absolute;left:688px;width:266px;display:flex;gap:6px;padding-bottom:6px;border-bottom:1px dotted #ccc}
.thumb{width:56px;height:56px;flex:none}
.item h3{font-weight:400;font-size:12.5px;color:var(--green-text);line-height:15px}
.item .sub{font-size:9.5px;color:var(--green-text);margin-left:2px}
.item p{font-size:9.2px;line-height:12.2px;color:var(--muted)}

.footer{left:0;top:928px;width:1050px;height:230px;background:linear-gradient(var(--footer-top),var(--footer-bottom));color:#ddd;font-family:"Arimo",sans-serif;border-top:1px solid #333}
.footer h4{position:absolute;font-family:"Cabin",sans-serif;font-weight:400;font-size:18px;color:#fff}
.footer ul{position:absolute;list-style:none;font-size:11px;line-height:20.1px}
.footer li:before{content:"•";margin-right:7px;color:#bbb}
.social{position:absolute;left:536px;top:56px;font-size:11.5px;color:#fff}
.social div{display:flex;align-items:center;gap:12px;height:30.6px}
.social span.sq{width:26px;height:26px;border-radius:3px}
.address{position:absolute;left:765px;top:55px;font-size:11.5px;line-height:15.8px;color:#fff}
.copyright{left:0;top:1174px;width:1050px;text-align:center;font-size:9.5px;color:#111}
</style>
</head>
<body>

<div class="abs brand"><span class="brand-mark"></span><span>RVD Worldwide<br>Limited</span></div>

<div class="abs lang">Your Language <div class="lang-select">English <span></span></div></div>

<div class="abs contact-top">
  <div><svg width="20" height="14" viewBox="0 0 20 14"><path d="M2 5c0-3 16-3 16 0v2h-4V5H6v2H2z" fill="#222"/><rect x="5" y="7" width="10" height="6" rx="1" fill="#222"/></svg>Call Now: (852) 2750 4418</div>
  <div><svg width="20" height="14" viewBox="0 0 20 14"><rect x="1" y="1" width="18" height="12" fill="#222"/><path d="M1 1l9 7 9-7" stroke="#fff" stroke-width="1.3" fill="none"/></svg>Email: sales@rvdboard.com</div>
</div>

<nav class="abs nav">
  <div class="nav-home"><svg width="24" height="22" viewBox="0 0 24 22"><path d="M12 2L2 11h3v9h5v-6h4v6h5v-9h3z" fill="#fff"/></svg></div>
  <ul>
    <li>Home</li><li>About Us</li><li>Workshop</li><li>Quality</li><li>Technology</li><li>Feedback</li><li>Accessories</li><li>Customer Service</li><li>Reviews</li><li>Contact Us</li>
  </ul>
</nav>

<section class="abs hero" role="img" aria-label="Close-up photograph of a printed circuit board with a microchip and capacitors">
  <div class="hero-caption">RVD is providing a RISK FREE supply of double sided and multi-layered printed circuit boards to our customers</div>
</section>

<h1 class="abs welcome">Welcome to <b>RVD International</b></h1>
<div class="abs about">
  <p>RVD Worldwide Limited (RVD) was set up in Hong Kong in 2007 by two Hong Kong entrepreneurs, Mr. Lok Fai Tam and Mr. Wai Ho. We acquired the single sided printed circuit board factory located in Dongguan City, Guangdong Province, China, from Valtor Corporation of the U.S. in 2007. In addition to RVD, Mr. Tam and Mr. Ho also own Brightrail Systems Company Limited, a semiconductor company based in Hong Kong since 1997 with a total investment of over US$100 million. Brightrail is engaged in the manufacturing of flexible substrates and the assembly of Micro Electro Mechanical Systems (MEMS).</p>
  <p>RVD has been awarded TS 16949 and ISO14000 certificates since 2009 and 2004 respectively.</p>
</div>
<div class="abs btn">Learn More</div>

<section class="abs clients">
  <div class="client" style="left:8px;top:47px;width:130px">Norvance</div>
  <div class="client" style="left:169px;top:47px;width:76px;background:none;color:#d2202a">Keltra</div>
  <div class="client" style="left:270px;top:43px;width:125px;background:#dde2ea;color:#1b3b78;font-size:14px">Tamaki Drive</div>
  <div class="client" style="left:431px;top:43px;width:90px;background:none;color:#0e8a55">Hoshiro</div>
  <div class="client" style="left:3px;top:103px;width:138px">Kazumi</div>
  <div class="client" style="left:152px;top:103px;width:73px;color:#111">Orin</div>
  <div class="client" style="left:233px;top:94px;width:101px;height:43px;color:#c62027">Veltross</div>
  <div class="client" style="left:337px;top:101px;width:209px;color:#111;font-size:15px;gap:6px"><span style="width:10px;height:10px;border-radius:50%;background:#d2202a"></span>Hartwell International</div>
</section>
<div class="abs clients-tab">These Products Featured On</div>

<h2 class="abs side-title">You may also like...</h2>

<article class="item" style="top:546px">
  <div class="thumb" role="img" aria-label="Field of grass under a sky" style="background:linear-gradient(#b8c9b0,#c7b55a 55%,#6d8a2a)"></div>
  <div><h3>Raw Materials</h3><p>Lorem Ipsum is simply dummy text of the printing and typesetting industry. Lorem Ipsum has been the industry's standard dummy text</p></div>
</article>
<article class="item" style="top:616px">
  <div class="thumb" role="img" aria-label="Copper wires and a hand tool" style="background:linear-gradient(135deg,#f4efe8,#d08a4e 60%,#a85a2a)"></div>
  <div><h3>Copper Thickness</h3><div class="sub">double slide</div><p>Lorem Ipsum is simply dummy text of the printing and typesetting industry. Lorem Ipsum</p></div>
</article>
<article class="item" style="top:690px">
  <div class="thumb" role="img" aria-label="Plating machinery in the factory" style="background:linear-gradient(135deg,#8e8f8c,#d7d6cf 55%,#6f706c)"></div>
  <div><h3>Plating</h3><p>Lorem Ipsum is simply dummy text of the printing and typesetting industry. Lorem Ipsum has been the industry's standard dummy text</p></div>
</article>
<article class="item" style="top:763px">
  <div class="thumb" role="img" aria-label="CNC machine punching a board" style="background:linear-gradient(135deg,#5a5f62,#c3c6c4 50%,#45494b)"></div>
  <div><h3>Punching And CNC Process</h3><p>Lorem Ipsum is simply dummy text of the printing and typesetting industry. Lorem Ipsum has been the industry's standard dummy text</p></div>
</article>
<article class="item" style="top:837px">
  <div class="thumb" role="img" aria-label="Green circuit board traces after V-cut" style="background:linear-gradient(135deg,#5fbf3c,#2f8c25 60%,#1f6b1a)"></div>
  <div><h3>V-Cut</h3><p>Lorem Ipsum is simply dummy text of the printing and typesetting industry. Lorem Ipsum has been the industry's standard dummy text</p></div>
</article>

<footer class="abs footer">
  <h4 style="left:99px;top:17px">Quick Links</h4>
  <ul style="left:96px;top:52px">
    <li>Home</li><li>About Us</li><li>Custom Engering</li><li>Automation</li><li>Workshop</li><li>About</li><li>Contact</li>
  </ul>
  <ul style="left:304px;top:51px">
    <li>Featured Product</li><li>Accumulation Tables</li><li>Slicer Project</li><li>Raw Materials</li><li>Punching and CNC Process</li><li>Engineering / Design Assistance</li><li>Platforms</li>
  </ul>
  <h4 style="left:534px;top:17px">Follow Us</h4>
  <div class="social">
    <div><span class="sq" style="background:#3b5b9a"></span>Follow us on Pagebook</div>
    <div><span class="sq" style="background:#3fa9d6"></span>Follow us on Chirper</div>
    <div><span class="sq" style="background:#1b7fb5"></span>Follow us on Workline</div>
    <div><span class="sq" style="background:#d0262a"></span>Follow us on Viewtube</div>
  </div>
  <h4 style="left:763px;top:17px">Contact</h4>
  <div class="address">
    RVD Worldwide Limited<br>28/F Harbour Crest<br>71 Marlow Road<br>Causeway Bay, HONG<br>KONG<br>
    <div style="margin-top:10px">Telephone: (852) 2750 4418<br>Fax: (852) 2750 4419</div>
    <div style="margin-top:13px">Email: sales@rvdboard.com</div>
  </div>
</footer>

<div class="abs copyright">COPYRIGHT - include a copyright statement © 2012 RVD Worldwide Limited, | All rights reserved</div>

</body>
</html>
```